Email Marketing Campaign Brief

We want to do an email marketing campaign around our consulting services. The attached documents provide back ground on our work but additional copy can be found below:

KV7pr is committed to helping you, the educator, make informed buying decisions based on local control and independent reviews through a simple, impartial and an effective approach.
In education, there exists a vast array of educational solutions – such as reading, science, language arts, and math curricula; school-wide reform programs; interventions; after-school programs; and new educational technologies. In the marketplace, providers could, and most do, claim to be able to improve educational outcomes and, in many cases, they all pretend to be supported by evidence. But a cursory review reveals that most evidence consists of poorly designed or advocacy-driven studies with some providers having such inadequate research as could only be described as case studies.

So the problem for State and local education officials is that they must sort through a myriad of such claims to decide which solutions merit consideration for their schools and classrooms. One US official stated the problem saying “many of these practitioners have seen interventions (solutions), introduced with great fanfare as being able to produce dramatic gains, come and go over the years, yielding little in the way of positive and lasting change – a perception confirmed by the flat achievement results over the past 30 years in the Federal Review of Scholastic Advancement long-term trend”

KV7pr is a process by which we make you, the educator, the locus of control

OUR Approach:
With four simple, yet highly effective steps, KV7pr guides educators through an informed buying process that’s based on local control and review.

Step 1 — Research, Review, and Evaluation Criteria

Step 2 — Cost / Benefit Analysis

Step 3 — Education Survey & Culture Scan

Step 4 — Negotiation & Representation

Target Market(s)

Education

Industry/Entity Type

Marketing

Font styles to use
Sans Serif

Colors
f9b46a
f37122

Requirements
Must have
• HTML format that can be used in an Email Campaign
Nice to have
• Additional Copy in Word

```html
<!DOCTYPE html>
<html lang="en">
<head>
<meta charset="utf-8">
<title>KV7pr — Research, Teaching, Learning</title>
<link rel="stylesheet" href="https://fonts.googleapis.com/css2?family=Titillium+Web:ital,wght@0,400;0,600;0,700;1,700&display=swap">
<style>
  :root {
    --orange: #f37122;
    --orange-light: #f9b46a;
    --ink: #1d1d1d;
    --paper: #ffffff;
    --stage: #ececec;
    --photo-blue: #3f6fc4;
    --photo-warm: #f2c46a;
  }
  * { box-sizing: border-box; margin: 0; padding: 0; }
  html, body { width: 1200px; height: 800px; overflow: hidden; background: var(--stage); }
  body { font-family: "Titillium Web", Arial, sans-serif; color: var(--ink); }

  .email {
    position: absolute; left: 100px; top: 20px;
    width: 1000px; height: 760px;
    background: var(--paper);
    overflow: hidden;
    box-shadow: 0 2px 10px rgba(0,0,0,.08);
  }

  .hero { position: relative; width: 1000px; height: 500px; }
  .hero-photo {
    position: absolute; inset: 0;
    background:
      linear-gradient(180deg, rgba(255,255,255,0) 62%, #fff 100%),
      linear-gradient(100deg, var(--photo-blue) 0%, #8fa9d6 30%, #f3d9b8 48%, var(--photo-warm) 62%, #e98a4a 82%, #d9c7b7 100%);
  }

  .brand-tab {
    position: absolute; left: 705px; top: 0;
    width: 250px; height: 200px;
  }
  .brand-tab svg { position: absolute; inset: 0; }
  .brand-name {
    position: absolute; top: 22px; left: 0; right: 0;
    display: flex; align-items: center; justify-content: center; gap: 10px;
    font-weight: 400; font-size: 46px; color: #fff; line-height: 1;
  }
  .brand-mark { width: 26px; height: 26px; background: #fff; }
  .brand-tagline {
    position: absolute; top: 92px; left: 0; right: 0; text-align: center;
    font-weight: 700; font-size: 17px; color: #fff;
  }

  .headline {
    position: absolute; left: 640px; top: 225px; width: 340px;
    font-weight: 700; font-style: italic; font-size: 44px; line-height: 1.1;
    color: #fff; text-shadow: 0 2px 6px rgba(0,0,0,.35);
  }

  .section-title {
    position: absolute; top: 455px; left: 0; width: 1000px;
    display: flex; align-items: center; justify-content: space-between;
  }
  .section-title .bar { width: 48px; height: 14px; background: var(--orange); }
  .section-title h2 {
    font-weight: 700; font-style: italic; font-size: 34px; color: var(--orange);
  }

  .copy {
    position: absolute; top: 540px; left: 30px; width: 940px;
    display: grid; grid-template-columns: 1fr 1fr; gap: 30px;
    font-size: 16px; line-height: 1.4; text-align: justify;
  }
  .copy p + p { margin-top: 6px; }
  .copy .brand-inline { color: var(--orange); font-weight: 700; }
</style>
</head>
<body>
  <main class="email">
    <section class="hero">
      <div class="hero-photo" role="img" aria-label="Photo of two smiling schoolgirls at a classroom desk with coloured pencils"></div>

      <div class="brand-tab">
        <svg width="250" height="200" viewBox="0 0 250 200" aria-hidden="true">
          <polygon points="0,0 250,0 250,150 125,200 0,150" fill="var(--orange)"/>
        </svg>
        <div class="brand-name"><span class="brand-mark"></span>KV7pr</div>
        <div class="brand-tagline">Research + Policy + Practice</div>
      </div>

      <h1 class="headline">We help you to build geniuses</h1>

      <div class="section-title">
        <span class="bar"></span>
        <h2>Research, Teaching, Learning</h2>
        <span class="bar"></span>
      </div>
    </section>

    <section class="copy">
      <div>
        <p>According to the Council of District School Leaders, our K12 education system has over $200 billion of annual spending power.</p>
        <p>Of that amount, an estimated $8 billion is spent by educators on products and services with the hope of an output that produces positive results for children. But with that come thousands of competing claims to sort through.</p>
      </div>
      <div>
        <p>KV7pr takes apart the provider-led reviews and long drawn out process of selecting a program solution and puts you in the drivers seat. From cultural scan to educator and community surveys, we help you make an informed, independent review and selection that's right for you students, teachers and administrators.</p>
        <p><span class="brand-inline">KV7pr</span> is a process by which we make you, the educator, the focus.</p>
      </div>
    </section>
  </main>
</body>
</html>
```